Website for an interior designer

We need a new website for Rosa Lynn Thackery whose new business name is Rosa Lynn Thackery Interiors. She is a residential interior designer with a mix of modern and contemporary tastes. We are in the process of overhauling her website which is +15 years old and not an accurate reflection of her tastes. The uploaded photos are from some of the houses she has done as well as her logo(s). We would need a section for "About Us" that would have a paragraph of text and bullets showing services and a gallery for photos (~12 total, more to come). A contract page would be optional. The client likes the feel/look of this website: https://www.corvenhollowdesign.example/ but doesn't want to copy it exactly.

Target Market(s)

Upscale home owners

Industry/Entity Type

Interior Design

Coding

Coded - Design and coding required

Number of Pages Required

4 page

Colors

Designer to choose only greyscale colors for use in the design.

Requirements
Must have
• Home page, about us page, gallery page, contact us page.

```html
<!DOCTYPE html>
<html lang="en">
<head>
<meta charset="utf-8">
<title>Contact — Rosa Lynn Thackery Interiors</title>
<link rel="stylesheet" href="https://fonts.googleapis.com/css2?family=Tinos&display=swap">
<style>
  :root {
    --ink: #6b6b6b;
    --ink-dark: #2e2e2e;
    --rule: #7a7a7a;
    --field-border: #a9a9a9;
    --block: #3d3d3d;
    --button: #4f4f4f;
    --paper: #ffffff;
    --footer: #fdfdfd;
    --footer-line: #ececec;
  }
  * { box-sizing: border-box; margin: 0; padding: 0; }
  html, body { width: 1200px; height: 875px; overflow: hidden; background: var(--paper); }
  body { position: relative; font-family: "Tinos", "Times New Roman", serif; color: var(--ink); }

  .brand {
    position: absolute; left: 55px; top: 24px;
    font-size: 15px; color: var(--ink-dark); letter-spacing: 0.5px;
  }

  .site-nav a {
    position: absolute; top: 20px; transform: translateX(-50%);
    font-size: 17.5px; color: var(--ink); text-decoration: none;
  }
  .site-nav .is-current::after {
    content: ""; position: absolute; left: 50%; top: 30px;
    width: 94px; height: 1px; background: var(--rule); transform: translateX(-50%);
  }

  .accent-block {
    position: absolute; left: 600px; top: 178px; width: 392px; height: 509px;
    background: var(--block); box-shadow: 0 2px 4px rgba(0,0,0,0.25);
  }
  .contact-card {
    position: absolute; left: 264px; top: 221px; width: 669px; height: 425px;
    background: var(--paper); box-shadow: 0 3px 6px rgba(0,0,0,0.22);
  }

  .section-title {
    position: absolute; top: 258px; width: 137px; text-align: center;
    font-size: 19px; font-weight: normal; color: var(--ink);
  }
  .section-title::after {
    content: ""; position: absolute; left: 0; top: 35px; width: 137px; height: 1px;
    background: var(--rule); box-shadow: 0 2px 3px rgba(0,0,0,0.15);
  }
  .title-message { left: 349px; }
  .title-info { left: 702px; }

  .field-label { position: absolute; left: 332px; font-size: 12.5px; color: var(--ink); }
  .field-input {
    position: absolute; left: 386px; width: 151px; height: 21px;
    border: 1px solid var(--field-border); background: var(--paper);
  }
  .field-area {
    position: absolute; left: 332px; top: 472px; width: 267px; height: 80px;
    border: 1px solid var(--field-border); background: var(--paper); resize: none;
  }
  .send-button {
    position: absolute; left: 332px; top: 582px; width: 121px; height: 27px;
    background: var(--button); color: #fff; border: none;
    font-family: "Tinos", "Times New Roman", serif; font-size: 14px;
    box-shadow: 0 2px 3px rgba(0,0,0,0.3);
  }

  .info-line { position: absolute; left: 701px; font-size: 12px; color: var(--ink); word-spacing: 1px; }

  .site-footer {
    position: absolute; left: 0; top: 825px; width: 1200px; height: 50px;
    background: var(--footer); border-top: 1px solid var(--footer-line);
  }
  .footer-text { position: absolute; font-size: 11px; color: var(--ink); }
  .footer-icon { position: absolute; }
</style>
</head>
<body>
  <div class="brand">Rosa Lynn Thackery Interiors</div>

  <nav class="site-nav">
    <a href="#" style="left:739px">Home</a>
    <a href="#" style="left:866px">About</a>
    <a href="#" style="left:993px">Gallery</a>
    <a href="#" class="is-current" style="left:1097px">Contact</a>
  </nav>

  <div class="accent-block"></div>
  <section class="contact-card"></section>

  <h2 class="section-title title-message">Send Message</h2>
  <h2 class="section-title title-info">Contact Info</h2>

  <label class="field-label" style="top:327px">Name :</label>
  <input class="field-input" type="text" style="top:326px">
  <label class="field-label" style="top:367px">Email :</label>
  <input class="field-input" type="email" style="top:367px">
  <label class="field-label" style="top:407px">Title :</label>
  <input class="field-input" type="text" style="top:407px">
  <label class="field-label" style="top:447px">Message</label>
  <textarea class="field-area"></textarea>
  <button class="send-button">Send</button>

  <p class="info-line" style="top:356px">Email :&nbsp; example@mail.com</p>
  <p class="info-line" style="top:402px">Phone :&nbsp; +1 222 333 4444</p>

  <footer class="site-footer">
    <span class="footer-text" style="left:386px; top:17px">© 2020-2020 All rights reserved</span>
    <svg class="footer-icon" style="left:656px; top:17px" width="15" height="15" viewBox="0 0 24 24" aria-hidden="true">
      <path fill="#6b6b6b" d="M6.6 10.8c1.4 2.8 3.8 5.1 6.6 6.6l2.2-2.2c.3-.3.7-.4 1-.2 1.1.4 2.3.6 3.6.6.6 0 1 .4 1 1V20c0 .6-.4 1-1 1C10.6 21 3 13.4 3 4c0-.6.4-1 1-1h3.5c.6 0 1 .4 1 1 0 1.3.2 2.5.6 3.6.1.3 0 .7-.2 1L6.6 10.8z"/>
    </svg>
    <span class="footer-text" style="left:674px; top:19px">+1 (222) 333-444</span>
    <svg class="footer-icon" style="left:778px; top:19px" width="16" height="12" viewBox="0 0 16 12" aria-hidden="true">
      <rect width="16" height="12" fill="#6b6b6b"/>
      <path d="M1 1l7 5.5L15 1" fill="none" stroke="#fdfdfd" stroke-width="1.2"/>
    </svg>
    <span class="footer-text" style="left:807px; top:18px">example@mail.com</span>
  </footer>
</body>
</html>
```